Stationery Required - Own Logo provided

Hi,

We are a retail company called 'Bramwick Carto Limited' based in the UK and would like some corporate stationery designed.

We have provided our Logo which we would like to use (Its attached to this brief)...

The designs must be orginal, professional, stylish and interesting!

Target Market(s)

We will use this stationery to communicate with our wholesale suppliers and employees, so it must have a 'professional' feel about it.

Industry/Entity Type

It Company

Requirements
Must have
• Must be professional, corporate, stylish and not to 'fussy'. we require ... Business card design, a4 letter, compliment slip. All designs must be supplied in a format where the text (address/telephone numbers etc..) can be edited, as we have alot of staff and operate out of several different premises.
Nice to have
• I would like a windows backround picture file supplied as well so we can integrate that onto our computer systems.

```html
<!DOCTYPE html>
<html lang="en">
<head>
<meta charset="utf-8">
<title>Bramwick Carto Limited – Stationery</title>
<link href="https://fonts.googleapis.com/css2?family=Arimo:ital,wght@0,400;0,700;1,400&display=swap" rel="stylesheet">
<style>
  :root {
    --green: #95c840;
    --green-dark: #2e5a1c;
    --wood-dark: #4e2a1e;
    --wood-mid: #6a3a2b;
    --card-green-a: #c3dd8c;
    --card-green-b: #dcedb5;
    --paper: #ffffff;
    --shadow: rgba(0,0,0,0.45);
  }
  html, body { margin: 0; padding: 0; overflow: hidden; }
  body {
    width: 900px; height: 1200px; position: relative;
    background: #ffffff;
    font-family: "Arimo", Arial, sans-serif;
  }
  .sheet { position: absolute; background: var(--paper); box-shadow: 4px 5px 6px var(--shadow); overflow: hidden; }
  .band { position: absolute; left: 0; right: 0; }
  .wood { background: linear-gradient(180deg, var(--wood-mid), var(--wood-dark) 50%, var(--wood-mid)); }
  .card-panel { background: linear-gradient(180deg, var(--card-green-a), var(--card-green-b) 50%, var(--card-green-a)); }
  .green-bar { background: var(--green); color: #fff; font-size: 14px; line-height: 20px; }
  .brand { position: absolute; display: flex; align-items: center; gap: 8px; }
  .brand-mark { background: var(--green-dark); }
  .brand-name { color: var(--green); font-weight: 400; white-space: nowrap; }
  .dot { margin: 0 6px; }

  /* Letterhead */
  .letterhead { left: 113px; top: 20px; width: 715px; height: 1010px; }
  .letterhead .top-wood { top: 0; height: 52px; }
  .letterhead .top-bar { top: 52px; height: 20px; text-align: right; padding-right: 12px; }
  .letterhead .brand { left: 10px; top: 95px; }
  .letterhead .brand-mark { width: 40px; height: 40px; }
  .letterhead .brand-name { font-size: 30px; }
  .letterhead .foot-bar { top: 937px; height: 21px; text-align: center; }
  .letterhead .foot-wood { top: 958px; height: 52px; }

  /* Business card */
  .business-card { left: 353px; top: 462px; width: 235px; height: 130px; }
  .business-card .brand { left: 4px; top: 6px; }
  .business-card .brand-mark { width: 32px; height: 32px; }
  .business-card .brand-name { font-size: 17px; }
  .business-card .edge-top { top: 48px; height: 7px; }
  .business-card .panel { top: 55px; height: 68px; }
  .business-card .edge-bottom { top: 123px; height: 7px; }
  .card-person { position: absolute; left: 14px; top: 78px; color: var(--green-dark); }
  .card-person .name { font-size: 11px; }
  .card-person .role { font-size: 8px; font-style: italic; }
  .card-contact { position: absolute; right: 6px; top: 70px; text-align: right; font-size: 8px; line-height: 11px; color: var(--green-dark); }
  .card-contact b { font-weight: 700; }

  /* Compliment slip */
  .comp-slip { left: 54px; top: 601px; width: 569px; height: 267px; }
  .comp-slip .top-wood { top: 0; height: 31px; }
  .comp-slip .top-bar { top: 31px; height: 18px; }
  .comp-slip .bottom-bar { top: 217px; height: 20px; }
  .comp-slip .bottom-wood { top: 237px; height: 30px; }
  .comp-slip .brand { left: 6px; top: 58px; }
  .comp-slip .brand-mark { width: 34px; height: 34px; }
  .comp-slip .brand-name { font-size: 24px; }
  .compliments { position: absolute; left: 58px; top: 104px; font-size: 14px; color: var(--green); }
  .slip-contact { position: absolute; right: 8px; top: 140px; text-align: right; }
  .slip-contact .name { font-size: 12px; line-height: 14px; color: var(--green-dark); }
  .slip-contact .role { font-size: 8px; line-height: 11px; font-style: italic; color: var(--green); margin-bottom: 6px; }
  .slip-contact .line { font-size: 8.5px; line-height: 10.5px; color: var(--green); }
  .slip-contact .line b { color: var(--green-dark); }
</style>
</head>
<body>

<section class="sheet letterhead" aria-label="A4 letterhead">
  <div class="band wood top-wood" role="img" aria-label="Dark wood texture band"></div>
  <div class="band green-bar top-bar">Colin Marsh<span class="dot">●</span><i>Company Director</i><span class="dot">●</span>hello@bramwickcarto.co.uk</div>
  <div class="brand"><span class="brand-mark"></span><span class="brand-name">Bramwick Carto Limited</span></div>
  <div class="band green-bar foot-bar">07700900461<span class="dot">●</span>17 Mill Lane, Ashby Cross, County Down BT30 4QN</div>
  <div class="band wood foot-wood" role="img" aria-label="Dark wood texture band"></div>
</section>

<section class="sheet business-card" aria-label="Business card">
  <div class="brand"><span class="brand-mark"></span><span class="brand-name">Bramwick Carto Limited</span></div>
  <div class="band wood edge-top" role="img" aria-label="Dark wood texture strip"></div>
  <div class="band card-panel panel" role="img" aria-label="Light green wood texture panel"></div>
  <div class="band wood edge-bottom" role="img" aria-label="Dark wood texture strip"></div>
  <div class="card-person"><div class="name">Colin Marsh</div><div class="role">Company Director</div></div>
  <div class="card-contact">
    <div><b>T.</b> 07700900461</div>
    <div><b>@.</b> hello@bramwickcarto.co.uk</div>
    <div><b>A.</b> 17 Mill Lane, Ashby Cross,</div>
    <div>County Down BT30 4QN</div>
  </div>
</section>

<section class="sheet comp-slip" aria-label="Compliment slip">
  <div class="band wood top-wood" role="img" aria-label="Dark wood texture band"></div>
  <div class="band green-bar top-bar"></div>
  <div class="brand"><span class="brand-mark"></span><span class="brand-name">Bramwick Carto Limited</span></div>
  <div class="compliments">With compliments</div>
  <div class="slip-contact">
    <div class="name">Colin Marsh</div>
    <div class="role">Company Director</div>
    <div class="line"><b>T.</b> 07700900461</div>
    <div class="line"><b>@.</b> hello@bramwickcarto.co.uk</div>
    <div class="line"><b>A.</b> 17 Mill Lane, Ashby Cross,</div>
    <div class="line">County Down BT30 4QN</div>
  </div>
  <div class="band green-bar bottom-bar"></div>
  <div class="band wood bottom-wood" role="img" aria-label="Dark wood texture band"></div>
</section>

</body>
</html>
```